Pulsewell Power sharing solutions, we offer different types of mobile charging stations for all ty

I need an app that shows all the locations that use our charging stations.
the app should show the following:

1. a map where client can see where all the stations are
2. a map that shows which one is the nearest charging station based on the persons location
3. a search tab where you can pick the city ( all will be based from sweden) and we will start with two cities: Gothenburg and Stockholm. So user will be able to pick the city and than get a list of all venues using our stations. along the way we will keep adding cities and countries but for now i need a design, something i can show potential customers on a power point how this app will work.
4. a list of different venue categories:
- restaurant
- café
- Festival
- Airport
- Library
- Night club
- Shopping center

Once client chooses the city, they can also choose what they are looking for and choose for example which restaurant to eat at based on if they have our charging station or not

you can of course improvise on ideas, if you come up with something and want to add to the app design thats ok, I'm up for suggestions.

in conclusion: the purpose for the app is for users to be able to search for charging stations or see where the nearest charging station is

Target Market(s)

Everyone

Requirements
Must have
• professional and simple design

```html
<!DOCTYPE html>
<html lang="en">
<head>
<meta charset="utf-8">
<title>Pulsewell Power – Station Finder Screens</title>
<link href="https://fonts.googleapis.com/css2?family=Roboto:wght@400;500;700&display=swap" rel="stylesheet">
<style>
  :root {
    --stage: #1c1c1c;
    --screen: #ffffff;
    --row: #f2f2f2;
    --divider: #ffffff;
    --ink: #3a3a3a;
    --muted: #555555;
    --blue: #3d6fb7;
    --orange: #f07d14;
    --brown: #4a3735;
    --sea: #93cd7f;
    --land: #f3f3f3;
    --grey-land: #d6d6d6;
    --field: #f1f1f1;
    --field-line: #d9d9d9;
  }
  * { box-sizing: border-box; margin: 0; padding: 0; }
  html, body { width: 1200px; height: 683px; overflow: hidden; }
  body { background: var(--stage); font-family: "Roboto", Arial, sans-serif; color: var(--ink); position: relative; }

  .screen { position: absolute; top: 16px; width: 366px; height: 651px; background: var(--screen); overflow: hidden; }
  .screen--city { left: 18px; }
  .screen--checkins { left: 416px; }
  .screen--detail { left: 813px; }

  .status-bar { position: absolute; top: 0; left: 0; right: 0; height: 28px; display: flex; align-items: center; justify-content: space-between; padding: 0 6px; font-size: 11px; background: var(--screen); z-index: 3; }
  .status-bar .signal { display: flex; gap: 2px; align-items: center; }
  .status-bar .signal i { width: 5px; height: 5px; border-radius: 50%; background: #222; display: block; }
  .status-bar .battery { display: flex; align-items: center; gap: 3px; }
  .status-bar .battery b { width: 22px; height: 10px; border: 1px solid #222; display: block; background: #222; box-shadow: inset 0 0 0 1px #fff; }

  .city-picker { position: absolute; top: 40px; left: 10px; width: 346px; height: 38px; background: var(--field); border: 1px solid var(--field-line); display: flex; align-items: center; justify-content: space-between; padding: 0 12px; font-size: 13px; font-weight: 700; color: var(--brown); }
  .city-picker .caret { width: 0; height: 0; border-left: 4px solid transparent; border-right: 4px solid transparent; border-top: 5px solid var(--brown); }

  .map { position: absolute; left: 0; right: 0; bottom: 0; background: linear-gradient(160deg, var(--sea) 0%, var(--land) 35%, var(--land) 55%, var(--grey-land) 70%, var(--sea) 100%); }
  .screen--city .map { top: 90px; }
  .screen--detail .map { top: 28px; background: linear-gradient(200deg, var(--sea) 0%, var(--sea) 40%, var(--land) 55%, var(--land) 85%, var(--grey-land) 100%); }

  .pin { position: absolute; display: block; }
  .pin svg { width: 100%; height: 100%; display: block; }

  .map-tools { position: absolute; bottom: 12px; right: 10px; display: flex; gap: 5px; }
  .map-tools .tool { width: 38px; height: 37px; background: var(--brown); display: flex; align-items: center; justify-content: center; }

  .label-tip { position: absolute; background: var(--brown); color: #fff; font-size: 7px; font-weight: 500; display: flex; align-items: center; justify-content: center; border-radius: 3px; }
  .label-tip::after { content: ""; position: absolute; bottom: -5px; left: 50%; margin-left: -3px; border-left: 3px solid transparent; border-right: 3px solid transparent; border-top: 5px solid var(--brown); }

  .page-header { position: absolute; top: 28px; left: 0; right: 0; height: 62px; display: flex; align-items: center; padding-left: 22px; gap: 12px; font-size: 13px; font-weight: 700; color: var(--brown); }
  .checkin-list { position: absolute; top: 90px; left: 0; right: 0; list-style: none; }
  .checkin { height: 57px; background: var(--row); border-bottom: 1px solid var(--divider); position: relative; }
  .checkin--open { height: 113px; background: var(--screen); }
  .checkin .pin { left: 24px; top: 12px; width: 24px; height: 31px; }
  .checkin .venue { position: absolute; left: 64px; top: 21px; font-size: 12px; color: #444; }
  .checkin .when { position: absolute; right: 25px; top: 20px; text-align: right; font-size: 9px; font-weight: 700; color: #333; }
  .checkin .when span { display: block; font-size: 6.5px; font-weight: 400; color: var(--muted); margin-top: 2px; }
  .checkin .details { position: absolute; left: 64px; top: 45px; width: 152px; font-size: 6px; line-height: 1.35; color: #555; }

  .detail-card { position: absolute; left: 75px; top: 321px; width: 256px; height: 86px; background: var(--brown); border-radius: 5px; color: #fff; }
  .detail-card::after { content: ""; position: absolute; bottom: -10px; left: 124px; border-left: 4px solid transparent; border-right: 4px solid transparent; border-top: 10px solid var(--brown); }
  .detail-card h2 { position: absolute; top: 9px; left: 0; right: 0; text-align: center; padding-left: 0; font-size: 11px; font-weight: 700; }
  .detail-card .card-icon { position: absolute; left: 12px; top: 27px; width: 44px; height: 44px; }
  .detail-card p { position: absolute; left: 63px; top: 27px; width: 180px; font-size: 6px; line-height: 1.45; }
</style>
</head>
<body>

<svg width="0" height="0" style="position:absolute">
  <defs>
    <symbol id="pin-blue" viewBox="0 0 24 32"><path d="M12 1C5.9 1 1 5.9 1 12c0 7.5 11 19 11 19s11-11.5 11-19C23 5.9 18.1 1 12 1z" fill="#3d6fb7"/><circle cx="12" cy="12" r="7.5" fill="#fff"/><path d="M8.5 8.5l7 7M15.5 8.5l-7 7" stroke="#3d6fb7" stroke-width="1.6" stroke-linecap="round"/></symbol>
    <symbol id="pin-orange" viewBox="0 0 24 32"><path d="M12 1C5.9 1 1 5.9 1 12c0 7.5 11 19 11 19s11-11.5 11-19C23 5.9 18.1 1 12 1z" fill="#f07d14"/><circle cx="12" cy="12" r="7.5" fill="#fff"/><circle cx="12" cy="12" r="3.5" fill="#f07d14"/></symbol>
    <symbol id="pin-plane" viewBox="0 0 24 32"><path d="M12 1C5.9 1 1 5.9 1 12c0 7.5 11 19 11 19s11-11.5 11-19C23 5.9 18.1 1 12 1z" fill="#3d6fb7"/><circle cx="12" cy="12" r="7.5" fill="#fff"/><path d="M7.5 12h9M12 8.5l3 3.5-3 3.5M9.5 10v4" stroke="#3d6fb7" stroke-width="1.5" fill="none" stroke-linecap="round"/></symbol>
    <symbol id="pin-plus" viewBox="0 0 24 32"><path d="M12 1C5.9 1 1 5.9 1 12c0 7.5 11 19 11 19s11-11.5 11-19C23 5.9 18.1 1 12 1z" fill="#3d6fb7"/><circle cx="12" cy="12" r="7.5" fill="#fff"/><path d="M12 8.5v7M8.5 12h7" stroke="#3d6fb7" stroke-width="1.6" stroke-linecap="round"/></symbol>
    <symbol id="pin-cart" viewBox="0 0 24 32"><path d="M12 1C5.9 1 1 5.9 1 12c0 7.5 11 19 11 19s11-11.5 11-19C23 5.9 18.1 1 12 1z" fill="#3d6fb7"/><circle cx="12" cy="12" r="7.5" fill="#fff"/><path d="M7.5 9h1.5l1.2 4.5h5l1.2-3.5H9.6" stroke="#3d6fb7" stroke-width="1.3" fill="none"/><circle cx="10.5" cy="15.3" r=".9" fill="#3d6fb7"/><circle cx="14.5" cy="15.3" r=".9" fill="#3d6fb7"/></symbol>
  </defs>
</svg>

<!-- City screen -->
<section class="screen screen--city">
  <div class="status-bar"><span class="signal"><i></i><i></i><i></i><i></i><i></i></span><span>9:41 AM</span><span class="battery">100% <b></b></span></div>
  <div class="city-picker">Choose City <span class="caret"></span></div>
  <div class="map" role="img" aria-label="Map of northern and central Europe showing charging station locations">
    <span class="pin" style="left:92px;top:62px;width:16px;height:21px"><svg><use href="#pin-blue"/></svg></span>
    <span class="pin" style="left:165px;top:55px;width:15px;height:19px"><svg><use href="#pin-orange"/></svg></span>
    <span class="pin" style="left:228px;top:98px;width:26px;height:34px"><svg><use href="#pin-orange"/></svg></span>
    <span class="pin" style="left:120px;top:128px;width:24px;height:31px"><svg><use href="#pin-cart"/></svg></span>
    <span class="pin" style="left:37px;top:154px;width:15px;height:19px"><svg><use href="#pin-orange"/></svg></span>
    <span class="pin" style="left:46px;top:199px;width:22px;height:28px"><svg><use href="#pin-plane"/></svg></span>
    <span class="pin" style="left:181px;top:240px;width:12px;height:15px"><svg><use href="#pin-blue"/></svg></span>
    <span class="pin" style="left:239px;top:277px;width:12px;height:15px"><svg><use href="#pin-blue"/></svg></span>
    <span class="pin" style="left:137px;top:352px;width:12px;height:16px"><svg><use href="#pin-blue"/></svg></span>
    <span class="pin" style="left:24px;top:340px;width:13px;height:16px"><svg><use href="#pin-orange"/></svg></span>
    <span class="pin" style="left:205px;top:334px;width:13px;height:16px"><svg><use href="#pin-orange"/></svg></span>
    <span class="pin" style="left:237px;top:359px;width:14px;height:18px"><svg><use href="#pin-plane"/></svg></span>
    <span class="pin" style="left:33px;top:384px;width:14px;height:18px"><svg><use href="#pin-orange"/></svg></span>
    <span class="pin" style="left:92px;top:380px;width:12px;height:15px"><svg><use href="#pin-blue"/></svg></span>
    <span class="pin" style="left:182px;top:374px;width:12px;height:15px"><svg><use href="#pin-blue"/></svg></span>
    <span class="pin" style="left:196px;top:409px;width:14px;height:18px"><svg><use href="#pin-orange"/></svg></span>
    <span class="pin" style="left:76px;top:420px;width:11px;height:14px"><svg><use href="#pin-blue"/></svg></span>
    <span class="pin" style="left:145px;top:431px;width:14px;height:18px"><svg><use href="#pin-orange"/></svg></span>
    <span class="pin" style="left:236px;top:421px;width:11px;height:14px"><svg><use href="#pin-blue"/></svg></span>
    <span class="pin" style="left:266px;top:448px;width:12px;height:15px"><svg><use href="#pin-blue"/></svg></span>
    <span class="pin" style="left:52px;top:460px;width:11px;height:14px"><svg><use href="#pin-blue"/></svg></span>
    <span class="pin" style="left:85px;top:472px;width:14px;height:18px"><svg><use href="#pin-orange"/></svg></span>
    <span class="pin" style="left:180px;top:462px;width:13px;height:16px"><svg><use href="#pin-blue"/></svg></span>
    <span class="pin" style="left:222px;top:461px;width:13px;height:16px"><svg><use href="#pin-orange"/></svg></span>
    <span class="pin" style="left:183px;top:490px;width:12px;height:15px"><svg><use href="#pin-blue"/></svg></span>
    <span class="pin" style="left:134px;top:512px;width:11px;height:14px"><svg><use href="#pin-orange"/></svg></span>
    <span class="pin" style="left:97px;top:538px;width:10px;height:13px"><svg><use href="#pin-blue"/></svg></span>
    <span class="pin" style="left:137px;top:538px;width:10px;height:13px"><svg><use href="#pin-blue"/></svg></span>
    <div class="label-tip" style="left:77px;top:268px;width:103px;height:21px">Restaurant</div>
    <span class="pin" style="left:122px;top:296px;width:12px;height:15px"><svg><use href="#pin-blue"/></svg></span>
    <div class="map-tools">
      <span class="tool"><svg width="22" height="22" viewBox="0 0 22 22"><circle cx="11" cy="11" r="7" fill="none" stroke="#fff" stroke-width="1.5"/><circle cx="11" cy="11" r="4" fill="#fff"/><path d="M11 1v3M11 18v3M1 11h3M18 11h3" stroke="#fff" stroke-width="1.5"/></svg></span>
      <span class="tool"><svg width="26" height="20" viewBox="0 0 26 20"><path d="M1 3l7-2 10 3 7-2v15l-7 2-10-3-7 2z M8 1v15M18 4v15" fill="none" stroke="#fff" stroke-width="1.2"/></svg></span>
    </div>
  </div>
</section>

<!-- Checkins screen -->
<section class="screen screen--checkins">
  <div class="status-bar"><span class="signal"><i></i><i></i><i></i><i></i><i></i></span><span>9:41 AM</span><span class="battery">100% <b></b></span></div>
  <header class="page-header"><svg width="14" height="10" viewBox="0 0 14 10"><path d="M13 5H2M5.5 1L1.5 5l4 4" stroke="#4a3735" stroke-width="1.6" fill="none"/></svg>Checkins</header>
  <ul class="checkin-list">
    <li class="checkin"><span class="pin"><svg><use href="#pin-blue"/></svg></span><span class="venue">Restaurant</span><span class="when">3day ago<span>Lorem Ipsum is simply.</span></span></li>
    <li class="checkin"><span class="pin"><svg><use href="#pin-orange"/></svg></span><span class="venue">Café</span><span class="when">3day ago<span>Lorem Ipsum is simply dummy.</span></span></li>
    <li class="checkin"><span class="pin"><svg><use href="#pin-orange"/></svg></span><span class="venue">Festival</span><span class="when">3day ago<span>Lorem Ipsum is simply.</span></span></li>
    <li class="checkin"><span class="pin"><svg><use href="#pin-plane"/></svg></span><span class="venue">Airport</span><span class="when">3day ago<span>Lorem Ipsum is simply dummy.</span></span></li>
    <li class="checkin"><span class="pin"><svg><use href="#pin-orange"/></svg></span><span class="venue">Library</span><span class="when">3day ago<span>Lorem Ipsum is simply.</span></span></li>
    <li class="checkin checkin--open"><span class="pin"><svg><use href="#pin-orange"/></svg></span><span class="venue">Night club</span><span class="when">3day ago<span>Lorem Ipsum is simply dummy.</span></span>
      <p class="details">Lorem Ipsum is simply dummy text of the printing and typesetting industry. Lorem Ipsum has been the industry's standard dummy text ever since the 1500s, when an unknown printer took a galley of type and scrambled it to make a type specimen book.</p></li>
    <li class="checkin"><span class="pin"><svg><use href="#pin-cart"/></svg></span><span class="venue">Shopping center</span><span class="when">3day ago<span>Lorem Ipsum is simply.</span></span></li>
    <li class="checkin"><span class="pin"><svg><use href="#pin-plus"/></svg></span><span class="venue">More</span><span class="when">3day ago<span>Lorem Ipsum is simply.</span></span></li>
    <li class="checkin"><span class="pin"><svg><use href="#pin-plane"/></svg></span><span class="venue">Airport</span><span class="when">3day ago<span>Lorem Ipsum is simply dummy</span></span></li>
  </ul>
</section>

<!-- Detail screen -->
<section class="screen screen--detail">
  <div class="status-bar"><span class="signal"><i></i><i></i><i></i><i></i><i></i></span><span>9:41 AM</span><span class="battery">100% <b></b></span></div>
  <div class="map" role="img" aria-label="Zoomed map of the Baltic region with nearby charging stations">
    <span class="pin" style="left:179px;top:-10px;width:58px;height:64px"><svg><use href="#pin-cart"/></svg></span>
    <span class="pin" style="left:-10px;top:8px;width:22px;height:28px"><svg><use href="#pin-orange"/></svg></span>
    <span class="pin" style="left:0;top:134px;width:48px;height:64px"><svg><use href="#pin-plane"/></svg></span>
    <span class="pin" style="left:308px;top:221px;width:26px;height:34px"><svg><use href="#pin-blue"/></svg></span>
    <span class="pin" style="left:190px;top:421px;width:26px;height:34px"><svg><use href="#pin-blue"/></svg></span>
    <span class="pin" style="left:115px;top:475px;width:26px;height:34px"><svg><use href="#pin-blue"/></svg></span>
    <span class="pin" style="left:338px;top:454px;width:23px;height:30px"><svg><use href="#pin-blue"/></svg></span>
    <span class="pin" style="left:-12px;top:480px;width:24px;height:32px"><svg><use href="#pin-orange"/></svg></span>
    <span class="pin" style="left:66px;top:556px;width:24px;height:31px"><svg><use href="#pin-blue"/></svg></span>
    <span class="pin" style="left:203px;top:574px;width:36px;height:46px"><svg><use href="#pin-orange"/></svg></span>
    <div class="map-tools">
      <span class="tool"><svg width="22" height="22" viewBox="0 0 22 22"><circle cx="11" cy="11" r="7" fill="none" stroke="#fff" stroke-width="1.5"/><circle cx="11" cy="11" r="4" fill="#fff"/><path d="M11 1v3M11 18v3M1 11h3M18 11h3" stroke="#fff" stroke-width="1.5"/></svg></span>
      <span class="tool"><svg width="26" height="20" viewBox="0 0 26 20"><path d="M1 3l7-2 10 3 7-2v15l-7 2-10-3-7 2z M8 1v15M18 4v15" fill="none" stroke="#fff" stroke-width="1.2"/></svg></span>
    </div>
  </div>
  <article class="detail-card">
    <h2>Restaurant</h2>
    <svg class="card-icon" viewBox="0 0 44 44"><path d="M6 6l32 32M38 6L6 38" stroke="#fff" stroke-width="5" stroke-linecap="round"/><ellipse cx="31" cy="13" rx="6" ry="9" transform="rotate(45 31 13)" fill="#fff"/></svg>
    <p>Lorem Ipsum is simply dummy text of the printing and typesetting industry. Lorem Ipsum has been the industry's standard dummy text ever since the 1500s, when an unknown printer took a galley of type and scrambled it to make a type specimen book.</p>
  </article>
</section>

</body>
</html>
```